Motivational Quotes Poster Series

This is a 3 poster design series for Ridgeway Haul Academy. The size of each poster should be 18 inches wide and 24 inches tall. The goal of these posters is to serve as motivational "signs" to be hung in the office area for the employees (not customers). These employees are instructors/teachers, teaching students how to drive semi trucks. While each design is a separate poster and design, we're posting as 1 project because we'd like some continuity between the series. Below we'll break down the details of all 3 posters...

Poster #1
Text that must appear on poster - "If You Want The Best Out Of Each Student" and "Give The Best Of You!" Note: While this text must appear on the poster, you can arrange in the layout as you see fit. For example, first line could be at top of poster and second line on bottom.

Poster #2
Text that must appear on poster - "Invest In People" and "Change Someone's Life" (same notes apply as in 1st poster)

Poster #3
Text that must appear on poster - "Today Is..." and "Just Another Day For You" and "The Most Important Day In Their Life" Note: This can be laid out on the poster however you see fit, but each phrase needs to be separate and it needs to flow.

Target Market(s)

Truck Driver Training Instructors - These are middle-aged, mostly male, masculine type personalities.

Industry/Entity Type

Training

Requirements
Must have
• Must have noted text from description
Must have working files (ie - PSD, EPS, AI, etc) provided
Must have common theme between each poster in series
Must have easy to read font and layout
Must have product dimensions of 18 inches (width) by 24 inches (height). If design uses full dimensions please include quarter inch bleed.
Nice to have
• Nice to have a trucking theme...related to trucking industry, but not over the top. Example - This could mean subtle injection of background tire tracks, but by no means are tire tracks required.

For inspiration, you can visit the site at http://www.ridgewayhaul.example. While you can use the colors of the site/logo, you can still branch out between each poster to try new colors within reason.

Note: While we've attached the logo to this project, it COULD be used but doesn't HAVE to be included in the design. The logo IS NOT a focal point. The phrases in the poster ARE the focal point.

```html
<!DOCTYPE html>
<html lang="en">
<head>
<meta charset="utf-8">
<title>Ridgeway Haul Academy — Give The Best Of You</title>
<link rel="stylesheet" href="https://fonts.googleapis.com/css2?family=Anton&display=swap">
<style>
  :root {
    --asphalt: #232323;
    --stripe: #f0a03a;
    --type: #f7ac45;
  }
  html, body {
    margin: 0;
    padding: 0;
    width: 900px;
    height: 1200px;
    overflow: hidden;
    background: var(--asphalt);
  }
  .poster {
    position: relative;
    width: 900px;
    height: 1200px;
    background: var(--asphalt);
    overflow: hidden;
    font-family: "Anton", Impact, sans-serif;
  }
  .grain {
    position: absolute;
    inset: 0;
    width: 900px;
    height: 1200px;
  }
  .lane-stripe {
    position: absolute;
    top: 0;
    height: 1200px;
    background: var(--stripe);
  }
  .lane-stripe--outer { left: 52px; width: 71px; }
  .lane-stripe--inner { left: 147px; width: 72px; }
  .quote {
    margin: 0;
    color: var(--type);
    font-size: inherit;
  }
  .quote__line {
    position: absolute;
    display: block;
    line-height: 1;
    white-space: nowrap;
    font-weight: 400;
    transform-origin: left top;
  }
  .quote__line--intro   { left: 280px; top: 165px; font-size: 59px;  transform: scaleX(1.14); }
  .quote__line--best    { left: 278px; top: 243px; font-size: 110px; transform: scaleX(1.30); }
  .quote__line--student { left: 280px; top: 376px; font-size: 47px;  transform: scaleX(1.27); }
  .quote__line--give    { left: 282px; top: 438px; font-size: 160px; transform: scaleX(1.33); }
  .quote__line--close   { left: 294px; top: 625px; font-size: 63px;  transform: scaleX(1.24); }
</style>
</head>
<body>
<main class="poster">
  <svg class="grain" viewBox="0 0 900 1200" aria-hidden="true">
    <filter id="asphalt-grain">
      <feTurbulence type="fractalNoise" baseFrequency="0.9" numOctaves="2" stitchTiles="stitch"/>
      <feColorMatrix type="saturate" values="0"/>
      <feComponentTransfer>
        <feFuncA type="linear" slope="0.12"/>
      </feComponentTransfer>
    </filter>
    <rect width="900" height="1200" filter="url(#asphalt-grain)"/>
  </svg>

  <div class="lane-stripe lane-stripe--outer"></div>
  <div class="lane-stripe lane-stripe--inner"></div>

  <h1 class="quote">
    <span class="quote__line quote__line--intro">If You Want</span>
    <span class="quote__line quote__line--best">The Best</span>
    <span class="quote__line quote__line--student">Out Of Each Student</span>
    <span class="quote__line quote__line--give">Give</span>
    <span class="quote__line quote__line--close">The Best Of You!</span>
  </h1>
</main>
</body>
</html>
```